Flyer für Onlineshop
Zielgruppe
Wir vertreiben 2 Komponentenlacke, wasserbasiert, auf Polyurethanharz Basis zur Sanierung von Fliesen vieles und mehr.
Aufgabenstellung
Wir möchten eine Fleyer speziell für die Fliesenfarben.
Das Design soll frisch, modern und ansprechend gestaltet sein. Wir möchten den Fleyer öffentlich auslegen aber auch an z.B Jugendherbergen, Kurhäuser ect. und privat Personen verteilen um darauf aufmerksam zu machen das es eine güstige alternative zum Neukauf gibt.
Auf dem Flyer soll in der Fliesenlack im Vordergrund stehen es darf aber kurz auf weitere Produkte aufmerksam gemacht werden.
für die Größe des Flyers habe ich keine genauen Vorstellungen lasse mich überraschen.
Sie finden die Informationen die Sie benötigen unter
www.ralbo-sonderlacke.com/farben-lacke/fliesenfarbe
Der Fleyer sollte die Maße DIN lang (105 x 210 mm) hoch / 4 Seiten
Aber auch andere Vorschläge sind Willkommen
Also Logo habe ich verschiedene jpg´s hochgeladen..leider ist die qualität nicht sehr gut aber vielleicht können Sie was damit anfangen.
Bei weiteren Fragen stehe ich Ihnen gerne zur Verfügung

```html
<!DOCTYPE html>
<html lang="de">
<head>
<meta charset="utf-8">
<title>Die Fliesenfarbe – Ralbo Sonderlacke</title>
<link rel="stylesheet" href="https://fonts.googleapis.com/css2?family=Oswald:wght@300;400&family=Open+Sans:wght@400;700&display=swap">
<style>
  :root {
    --brand-blue: #1d5ca8;
    --accent-red: #c8381f;
    --panel-grey: #d8d8d8;
    --text: #3a3a3a;
    --heading: #2b2b2b;
    --paper: #ffffff;
  }
  * { margin: 0; padding: 0; box-sizing: border-box; }
  html, body { width: 1137px; height: 1200px; overflow: hidden; background: var(--paper); }
  body { position: relative; font-family: "Open Sans", Arial, sans-serif; color: var(--text); }

  .corner-mark { position: absolute; left: 32px; top: 0; width: 36px; height: 56px; background: var(--brand-blue); }

  .intro { position: absolute; left: 70px; top: 78px; width: 492px; }
  .intro__title {
    font-family: "Oswald", "Arial Narrow", sans-serif; font-weight: 300;
    font-size: 52px; line-height: 60px; letter-spacing: 3px; color: var(--heading);
  }
  .intro__title .initial { color: var(--accent-red); font-weight: 400; }
  .intro__question { font-weight: 700; font-size: 16px; line-height: 22px; margin-top: 2px; color: var(--heading); white-space: nowrap; }
  .body-copy { font-size: 15.6px; line-height: 33px; text-align: justify; }
  .body-copy b { font-weight: 700; }
  .intro .body-copy { margin-top: 30px; }

  .tiles-photo { position: absolute; left: 70px; top: 444px; width: 480px; height: 266px;
    background: linear-gradient(135deg, #e6d7c0 0%, #b5582e 35%, #d8c4a4 60%, #9b4a2a 85%, #e4d6c2 100%); }
  .tiles-bar { position: absolute; left: 36px; top: 580px; width: 34px; height: 130px; background: var(--brand-blue); }

  .usage { position: absolute; left: 70px; top: 722px; width: 492px; }

  .side-panel { position: absolute; left: 588px; top: 56px; width: 549px; height: 1144px; background: var(--panel-grey); }
  .bath-photo { position: absolute; left: 618px; top: 86px; width: 472px; height: 268px;
    background: linear-gradient(160deg, #6cc1ea 0%, #1b7fc4 55%, #0d5c98 100%); }
  .bath-bar { position: absolute; left: 1060px; top: 86px; width: 30px; height: 264px; background: var(--brand-blue); }

  .ready-title { position: absolute; left: 618px; top: 364px; width: 480px;
    font-family: "Oswald", "Arial Narrow", sans-serif; font-weight: 300;
    font-size: 32px; letter-spacing: 1.5px; color: var(--brand-blue); line-height: 44px; white-space: nowrap; }
  .ready-sub { position: absolute; left: 618px; top: 408px; font-weight: 700; font-size: 15.6px; color: var(--heading); }

  .product-card { position: absolute; left: 618px; top: 452px; width: 472px; height: 748px; background: var(--paper); }
  .finish-bar { position: absolute; left: 620px; top: 468px; width: 22px; height: 92px; background: var(--brand-blue); }
  .finish-list { position: absolute; left: 660px; top: 470px; list-style: none; font-size: 15.6px; line-height: 34px; }
  .product-card__copy { position: absolute; left: 630px; top: 574px; width: 458px; }

  .wash-photo { position: absolute; left: 618px; top: 896px; width: 472px; height: 284px;
    background: linear-gradient(120deg, #f1e6d6 0%, #c79a6c 45%, #6a4a33 100%); }
  .wash-bar { position: absolute; left: 590px; top: 896px; width: 28px; height: 160px; background: var(--brand-blue); }
</style>
</head>
<body>
  <div class="corner-mark"></div>

  <section class="intro">
    <h1 class="intro__title"><span class="initial">D</span>IE FLIESENFARBE</h1>
    <p class="intro__question">Ihres Bades oder Ihrer Küche gefällt Ihnen nicht mehr?</p>
    <p class="body-copy">Das ist kein Grund zum Verzagen, denn mit dem Fliesenlack aus dem <b>Ralbo-Sonderlacke-Sortiment</b>, kann Ihr Bad und Ihre Küche schon bald <b>in Ihrer Lieblingsfarbe</b> erstrahlen. Verzichten Sie darauf, die in die Jahre gekommenen Fliesen <b>abzuschlagen</b> und anschließend <b>neue Fliesen verlegen</b> zu lassen! So eine <b>Renovierung kostet</b> nicht nur sehr viel Geld, sie verursacht auch viel <b>Staub und Lärm</b>.</p>
  </section>

  <div class="tiles-bar"></div>
  <div class="tiles-photo" role="img" aria-label="Fliesen in Terrakotta- und Beigetönen, diagonal angeordnet"></div>

  <section class="usage">
    <p class="body-copy">Ob in <b>Bad</b>, <b>Küche</b> oder <b>Lagerraum</b>, Fliesen haben ohne Zweifel einen hohen praktischen Nutzen. Direkt nach dem Kauf findet man sie meist sehr schön. <b>Mit der Zeit jedoch verblasst oft ihr Glanz oder ihr Design kommt aus der Mode.</b> Es ist nicht unüblich, dass sich der persönliche Geschmack mit den Jahren wandelt. Wer Ralbo Fliesenfarbe verwendet, begegnet diesem Umstand, <b>ohne eine aufwändige Sanierung</b> mit teuren neuen Fliesen vornehmen zu müssen. <b>Lärm, Staub und Schmutz</b> durch einen Fliesenwechsel <b>müssen nicht sein</b>, denn unsere Fliesenlacke <b>haften und decken sehr gut</b>, wobei sie <b>wasserverdünnbar auf der Basis einer Kunststoffdispersion</b> sind. Gegen <b>Licht, Wetter und Chemikalien bestehen die Spezialfarben ebenfalls.</b> Je nach Variante bleibt der Farbton dabei <b>matt</b> oder <b>glänzt</b> ansprechend.</p>
  </section>

  <aside class="side-panel"></aside>
  <div class="bath-photo" role="img" aria-label="Modernes Badezimmer mit blau gefliesten Wänden und weißem Waschtisch"></div>
  <div class="bath-bar"></div>

  <h2 class="ready-title">GEBRAUCHSFERTIGE FLIESENFARBEN</h2>
  <p class="ready-sub">in vielen schönen Farbvariationen</p>

  <div class="product-card"></div>
  <div class="finish-bar"></div>
  <ul class="finish-list">
    <li>seidenglänzend für ein apartes Badezimmer</li>
    <li>matt für Keller oder Garage</li>
    <li>hochglänzend für Bad oder Küche</li>
  </ul>
  <p class="body-copy product-card__copy">Dabei stehen <b>zahlreiche Farbtöne</b> zur Auswahl, damit für jeden Möbelstil und jeden Geschmack das Passende gefunden werden kann. Neben <b>helleren und dunkleren</b> Varianten sind <b>kalte und warme Töne</b> verfügbar. Bevor der Decklack aufgetragen werden kann, sind eine reinigende Vorbehandlung, das Trocknen und der Auftrag der Grundierung nötig. Die dafür nötigen Produkte lassen sich separat <b>in unserem Onlineshop</b> erwerben.<br>Wir beraten Sie gerne! Besuchen Sie uns einfach auf <b>www.ralbo-sonderlacke.com</b></p>

  <div class="wash-bar"></div>
  <div class="wash-photo" role="img" aria-label="Helles Badezimmer mit Holzwaschtisch, Spiegel und Glasdusche"></div>
</body>
</html>
```